Insert sheet for our Dog Food Package

We need an information sheet to go inn our pet food package, with branding, and information on ingredients, nutrition and feeding guidance. We will also need two additional items which will be a variation on the label design:
1) Label for package (detailed label about us and our food)
2) Label for outer shipping box (simple label for branding)
We will start with the information, insert page. The winning designer will then deliver the package and box labels as simplified versions of the same graphical theme.
I have attached samples of an earlier drafts of the insert piece. Please disregard the style, form and colors of the examples given. THEY ARE ONLY THERE TO SHOW WHAT INFORMATION SHOULD BE INCLUDED. All colors and style should be from our logo (attached). All graphics, font styles, and placement of elements need to be YOUR creative design - not a copy of the sample we gave. PLEASE READ THIS AND PLEASE DO NOT SUBMIT ANY VARIATION OF THE EXAMPLES!!!!!!!

Target Market(s)

Pet Owners

Industry/Entity Type

Pet Food

Colors
EB3D1F
EC4F4E
F09395
F8D3D4
FCEDEE

Requirements
Must have
• All new design. New colors (based in the palette of our logo), new graphics, new fonts, new placement of elements.
Should not have
• Please disregard the style, form and colors of the examples given. THEY ARE ONLY THERE TO SHOW WHAT INFORMATION SHOULD BE INCLUDED.

```html
<!DOCTYPE html>
<html lang="en">
<head>
<meta charset="utf-8">
<title>Kindra – Insert Sheet</title>
<link href="https://fonts.googleapis.com/css2?family=Ubuntu:wght@400;500;700&display=swap" rel="stylesheet">
<style>
  :root {
    --brand-red: #ae2127;
    --deep-brown: #3d1512;
    --paper: #ffffff;
    --paper-shade: #e6e7e9;
  }
  * { box-sizing: border-box; margin: 0; padding: 0; }
  html, body { width: 968px; height: 1200px; overflow: hidden; background: #d1d3d4; }
  body { font-family: 'Ubuntu', sans-serif; }
  .sheet { position: relative; width: 968px; height: 1200px; overflow: hidden;
    background: linear-gradient(90deg, var(--paper) 70%, var(--paper-shade) 100%); }

  /* left info column */
  .info-panel { position: absolute; left: 0; top: 0; width: 500px; height: 1200px; background: var(--brand-red); color: var(--paper); }
  .info-title { position: absolute; left: 0; top: 96px; width: 500px; text-align: center;
    font-weight: 700; font-size: 41px; line-height: 52px; letter-spacing: 0.5px; }
  .info-box { position: absolute; left: 39px; width: 430px; border: 3px solid var(--paper); }
  .info-box__lead { background: var(--paper); color: var(--brand-red); font-weight: 700; font-size: 21px;
    text-align: center; display: flex; align-items: center; justify-content: center; }
  .info-box__heading { font-size: 25px; text-align: center; border-bottom: 3px solid var(--paper); }

  .nutrition { top: 227px; height: 424px; }
  .nutrition .info-box__lead { height: 60px; }
  .nutrition .info-box__heading { height: 59px; line-height: 56px; border-top: 3px solid var(--paper); }
  .analysis { display: grid; grid-template-columns: 1fr 1fr; font-size: 19px; font-weight: 500; }
  .analysis__cell { height: 31px; display: flex; justify-content: space-between; align-items: center;
    padding: 0 14px 0 29px; border-bottom: 3px solid var(--paper); }
  .analysis__cell:nth-child(odd) { border-right: 3px solid var(--paper); }
  .analysis__cell:nth-child(even) { padding-left: 14px; padding-right: 26px; }
  .ingredients { font-size: 17.5px; line-height: 24.5px; text-align: center; padding: 15px 14px 0; }

  .feeding { top: 675px; height: 534px; height: 432px; }
  .feeding .info-box__lead { height: 62px; }
  .feeding-plan__title { font-size: 24px; padding: 15px 0 0 21px; }
  .feeding-row { display: flex; font-size: 19px; padding-left: 24px; }
  .feeding-row span:first-child { width: 267px; }
  .feeding-row--head { font-weight: 500; font-size: 22px; padding-top: 12px; height: 47px; border-bottom: 3px solid var(--paper); }
  .feeding-group { border-bottom: 3px solid var(--paper); padding: 6px 0 5px; }
  .feeding-group:last-child { border-bottom: none; }
  .feeding-group .feeding-row { line-height: 29px; }

  /* right brand column */
  .brand-frame { position: absolute; left: 500px; top: 29px; width: 439px; height: 1141px; border: 8px solid var(--deep-brown); border-left: none; }
  .brand-mark { position: absolute; left: 535px; top: 95px; }
  .brand-name { position: absolute; left: 520px; top: 490px; width: 380px; text-align: center;
    font-weight: 700; font-size: 82px; letter-spacing: 6px; color: var(--brand-red); line-height: 1; }

  .story { position: absolute; left: 513px; top: 680px; width: 405px; color: var(--brand-red); }
  .story__title { font-weight: 700; font-size: 40px; display: flex; align-items: flex-end; gap: 6px; }
  .story__title::after { content: ""; flex: 1; height: 2px; background: var(--brand-red); margin-bottom: 8px; }
  .story__lead { font-weight: 500; font-size: 27px; line-height: 35px; margin-top: 16px; letter-spacing: -0.2px; }
  .story__quote { font-size: 18.5px; line-height: 24px; margin-top: 20px; }
</style>
</head>
<body>
<main class="sheet">
  <section class="info-panel">
    <h1 class="info-title">PREPARED WITH<br>LOVE FOR SHADOW</h1>

    <div class="info-box nutrition">
      <p class="info-box__lead">We Prepared the best for shadow</p>
      <h2 class="info-box__heading">NUTRITIONAL INFORMATION</h2>
      <div class="analysis">
        <div class="analysis__cell"><span>Protein:</span><span>15%</span></div>
        <div class="analysis__cell"><span>Total Fat:</span><span>9.5%</span></div>
        <div class="analysis__cell"><span>Crude Fiber:</span><span>2.0%</span></div>
        <div class="analysis__cell"><span>Moisture:</span><span>72%</span></div>
      </div>
      <p class="ingredients">Potassium Citrate, DiCalcium Phosphate, Calcium Carbonate, Garbanzo Beans, Choline Bitartrate, Taurine, Salt, Zinc Proteinate, Magnesium Oxide, Iron Proteinate, Vitamin B-12, Selenium, Niacin, Riboflavin, Calcium Panthothenate, Thiamine, Vitamin A, Vitamin D, Calcium Lodate, Vitamin B6, Folic Acid</p>
    </div>

    <div class="info-box feeding">
      <p class="info-box__lead">How much should i feed shadow?</p>
      <h2 class="feeding-plan__title">RECOMMENDED FEEDING PLAN</h2>
      <div class="feeding-row feeding-row--head"><span>Approximate weight</span><span>Full meal</span></div>
      <div class="feeding-group">
        <div class="feeding-row"><span>&lt;20 lbs</span><span>110 g</span></div>
      </div>
      <div class="feeding-group">
        <div class="feeding-row"><span>20-29 lbs</span><span>200 g</span></div>
        <div class="feeding-row"><span>30-39 lbs</span><span>250 g</span></div>
        <div class="feeding-row"><span>40-54 lbs</span><span>300 g</span></div>
      </div>
      <div class="feeding-group">
        <div class="feeding-row"><span>50-69 lbs</span><span>350 g</span></div>
        <div class="feeding-row"><span>70-85 lbs</span><span>400 g</span></div>
      </div>
      <div class="feeding-group">
        <div class="feeding-row"><span>85+ lbs</span><span>500 g</span></div>
      </div>
    </div>
  </section>

  <section>
    <div class="brand-frame"></div>
    <svg class="brand-mark" width="346" height="346" viewBox="0 0 346 346" role="img" aria-label="Kindra brand circle">
      <circle cx="173" cy="173" r="166" fill="var(--brand-red)" stroke="var(--deep-brown)" stroke-width="11"/>
    </svg>
    <p class="brand-name">KINDRA</p>

    <article class="story">
      <h2 class="story__title">OUR STORY</h2>
      <p class="story__lead">We Revolutionzed the industry. Not Formulated to meed a minimum standard, but to develop the maximum health of the whole dog.</p>
      <p class="story__quote">“we didn’t just set about to create a food that will ‘pass a minimum standard”. We set out to revolutionize the industry by creating a food that is designed with Superfoods, Wholesie Grains, and Powerful Oil to help your dog achieve their maximum health, happiness andlongevity.</p>
    </article>
  </section>
</main>
</body>
</html>
```